Zentrix Banner Grid Ads for Custom Software Company

We need some images for display on the Zentrix Banner Grid. Need a collection of them at different sizes.

This is for a custom software development company that specializes in small to medium size businesses.

PLEASE PLEASE PLEASE GET CREATIVE! That is the point! Something very typical and plain will not win!

Target Market(s)

Small and Medium sized businesses looking for custom software development services

Industry/Entity Type

Computer Software

Font styles to use
Serif
Sans Serif

Requirements
Must have
• Medium Rectangle (300×250)
• Large Rectangle (336×280)
• Leaderboard (728×90)
• Half Page (300×600)
• Large Mobile Banner (320×100)
• Needs to stand out, but not be obnoxious
• Needs to flow with the website design and colors (does not need to be the same colors, just needs to work together)
• Must have specific call to action (schedule appointment or read more are options, but feel free to make up more)
Nice to have
• Logo integration
• Adobe Illustrator files with artboards/exports for the different sizes
Should not have
• Should not have more than 20% text
• Don't steal from the slides on the website. We want "read more" to mean read more, not more of the same.

```html
<!DOCTYPE html>
<html lang="en">
<head>
<meta charset="utf-8">
<title>Zentrix Banner Grid – Half Page Banner, Option 2</title>
<link rel="stylesheet" href="https://fonts.googleapis.com/css2?family=Barlow:wght@400;500;600;700&family=Barlow+Semi+Condensed:wght@500;600;700&display=swap">
<style>
  :root {
    --paper: #ffffff;
    --sky: #27c8ee;
    --royal: #0656a8;
    --label-blue: #0a55a8;
    --white: #ffffff;
    --suit-dark: #3a3d40;
    --suit-mid: #6b6e70;
  }
  * { margin: 0; padding: 0; box-sizing: border-box; }
  html, body {
    width: 1200px;
    height: 1200px;
    overflow: hidden;
    background: var(--paper);
  }
  .canvas {
    position: relative;
    width: 1200px;
    height: 1200px;
    background: var(--paper);
    font-family: "Barlow", "Helvetica Neue", Arial, sans-serif;
  }
  .option-label {
    position: absolute;
    left: 114px;
    top: 566px;
    font-size: 60px;
    font-weight: 500;
    letter-spacing: 2px;
    color: var(--label-blue);
    line-height: 1;
  }
  .banner {
    position: absolute;
    left: 594px;
    top: 0;
    width: 606px;
    height: 1200px;
    background: var(--sky);
    overflow: hidden;
  }
  .banner-panel {
    position: absolute;
    left: 84px;
    top: 0;
    width: 436px;
    height: 812px;
    background: var(--royal);
  }
  .brand {
    position: absolute;
    left: 61px;
    top: 55px;
    display: flex;
    align-items: center;
    gap: 18px;
  }
  .brand-mark {
    width: 76px;
    height: 76px;
    background: var(--white);
  }
  .brand-name {
    font-size: 60px;
    font-weight: 400;
    color: var(--white);
    line-height: 1;
  }
  .tagline {
    position: absolute;
    left: 0;
    top: 180px;
    width: 100%;
    text-align: center;
    font-family: "Barlow Semi Condensed", "Barlow", Arial, sans-serif;
    font-size: 35px;
    font-weight: 600;
    line-height: 42px;
    color: var(--white);
  }
  .headline {
    position: absolute;
    left: 0;
    top: 400px;
    width: 436px;
    text-align: center;
    font-family: "Barlow Semi Condensed", "Barlow", Arial, sans-serif;
    font-size: 54px;
    font-weight: 500;
    line-height: 50px;
    letter-spacing: 1px;
    color: var(--white);
  }
  .cta-button {
    position: absolute;
    left: 36px;
    top: 722px;
    width: 360px;
    height: 56px;
    background: var(--sky);
    color: var(--white);
    font-family: "Barlow Semi Condensed", "Barlow", Arial, sans-serif;
    font-size: 26px;
    font-weight: 700;
    letter-spacing: 0.5px;
    display: flex;
    align-items: center;
    justify-content: center;
    box-shadow: 0 4px 6px rgba(0, 0, 0, 0.25);
  }
  .presenter-photo {
    position: absolute;
    left: 30px;
    top: 812px;
    width: 544px;
    height: 388px;
    background: linear-gradient(180deg, var(--suit-mid) 0%, var(--suit-dark) 100%);
  }
</style>
</head>
<body>
  <main class="canvas">
    <p class="option-label">OPTION 2</p>

    <section class="banner" aria-label="Half page banner">
      <div class="banner-panel">
        <div class="brand">
          <span class="brand-mark" aria-hidden="true"></span>
          <span class="brand-name">Veltrane</span>
        </div>

        <p class="tagline">Custom Softwares<br>for your business</p>

        <h1 class="headline">THE POWER OF<br>PRODUCTIVITY IN<br>YOUR HANDS</h1>

        <div class="cta-button">BOOST PRODUCTIVITY</div>
      </div>

      <div class="presenter-photo" role="img" aria-label="Businessman in a grey suit holding a glowing tablet in both hands, shown from the chest down"></div>
    </section>
  </main>
</body>
</html>
```